Post COVID-19 Infographic - As the economy begins to rebound, you need to be ready to upgrade your f

Due to the COVID-19 Pandemic, many of these businesses are shut down or operating with essential staff while the remaining personnel are working from home.

As we are reaching the peak of the pandemic, many businesses are starting to think about what they need to do in their facilities to retrofit them and make them safe for their employees and customers in a post COVID-19 world.
This assignment is about developing an infographic that will provide our current and potential customers with information about the old world, and the new world. This needs to be interesting, informational, and viral (i.e.- content is so compelling folks will share with friends, colleagues and other businesses.

Please see attached for a full fledged creative brief.

Target Market(s)

Distribution Centers, manufacturers, Multi-family Housing property managers, Home Owner Associations, Small to Medium Sized Businesses

Industry/Entity Type

Distributor

Font styles to use
Sans Serif

Requirements
Must have
• Graphical, easy to understand, fun to read, trigger thinking, reader would want to share with friends, colleagues, online

Colors should be similar to color palette used on our website www.brentwickmercantile.com
Nice to have
• Iconography
Should not have
• Should not appear like we are trying to sell. Should look informational but should be clear that we can supply those products

```html
<!DOCTYPE html>
<html lang="en">
<head>
<meta charset="utf-8">
<title>Old World vs New World – Post COVID-19 Workplace</title>
<link href="https://fonts.googleapis.com/css2?family=Roboto:wght@500;700;900&display=swap" rel="stylesheet">
<style>
  :root{
    --red:#e1262d;
    --red-deep:#8f1a22;
    --blue:#1f6db3;
    --blue-deep:#163f6e;
    --navy:#1b3a66;
    --icon:#f6cf1c;
    --icon-shade:#c79a10;
    --white:#ffffff;
    --line:rgba(255,255,255,.18);
  }
  *{margin:0;padding:0;box-sizing:border-box}
  html,body{width:695px;height:1200px;overflow:hidden;background:var(--white)}
  body{font-family:"Roboto",Arial,sans-serif;color:var(--white)}
  .infographic{position:relative;width:695px;height:1200px}

  .masthead{position:relative;height:74px;background:var(--white)}
  .masthead h2{position:absolute;top:20px;font-weight:900;font-size:36px;letter-spacing:.5px;line-height:1}
  .masthead .old{left:14px;width:320px;text-align:center;color:var(--red)}
  .masthead .new{left:362px;width:320px;text-align:center;color:var(--navy)}
  .masthead .divider{position:absolute;left:346px;top:12px;width:3px;height:54px;background:var(--navy)}

  .comparison{position:relative;height:1024px}
  .row{position:relative;height:128px;border-top:1px solid var(--line)}
  .row .side{position:absolute;top:0;height:100%}
  .row .side-old{left:0;width:348px}
  .row .side-new{left:348px;width:347px}
  .label{position:absolute;top:50%;transform:translate(-50%,-50%);text-align:center;
    font-weight:700;font-size:19px;line-height:1.2;text-transform:uppercase;white-space:nowrap}
  .label.old{left:139px}
  .label.new{left:549px}

  .row:nth-child(1) .side-old{background:linear-gradient(90deg,#e8262e,#d92229)}
  .row:nth-child(2) .side-old{background:linear-gradient(90deg,#e1242c,#cc2028)}
  .row:nth-child(3) .side-old{background:linear-gradient(90deg,#d62229,#c01f27)}
  .row:nth-child(4) .side-old{background:linear-gradient(90deg,#cb2027,#b31d25)}
  .row:nth-child(5) .side-old{background:linear-gradient(90deg,#bf1e26,#a71c24)}
  .row:nth-child(6) .side-old{background:linear-gradient(90deg,#b31d25,#9c1b23)}
  .row:nth-child(7) .side-old{background:linear-gradient(90deg,#a61c24,#931a22)}
  .row:nth-child(8) .side-old{background:linear-gradient(90deg,#9a1b23,var(--red-deep))}
  .row:nth-child(1) .side-new{background:linear-gradient(90deg,#2a79bf,#2069b0)}
  .row:nth-child(2) .side-new{background:linear-gradient(90deg,#2572b8,#1d63a8)}
  .row:nth-child(3) .side-new{background:linear-gradient(90deg,#216bb0,#1b5d9f)}
  .row:nth-child(4) .side-new{background:linear-gradient(90deg,#1f65a8,#1a5796)}
  .row:nth-child(5) .side-new{background:linear-gradient(90deg,#1d5e9e,#19518c)}
  .row:nth-child(6) .side-new{background:linear-gradient(90deg,#1b5794,#184b82)}
  .row:nth-child(7) .side-new{background:linear-gradient(90deg,#1a508a,#174578)}
  .row:nth-child(8) .side-new{background:linear-gradient(90deg,#184a80,var(--blue-deep))}

  .icon{position:absolute;top:50%;transform:translate(-50%,-50%)}
  .icon-fill{background:var(--icon);border-radius:6px}
  .icon.left{left:243px}
  .icon.right{left:400px}
  .icon.center{left:348px}

  .count{position:absolute;top:50%;transform:translate(-50%,-50%);font-weight:900;font-size:58px;line-height:1}
  .count.old{left:268px}
  .count.new{left:426px}
  .row.supplies .label.old{left:122px}
  .row.supplies .label.new{left:572px}
  .row.traffic .label.new{left:548px;font-size:15px;white-space:normal;width:250px}

  .sponsors{position:relative;height:102px;background:var(--white)}
  .brand{position:absolute;display:flex;align-items:center;gap:8px}
  .brand-primary{left:16px;top:22px}
  .brand-primary .mark{width:18px;height:18px;background:var(--navy)}
  .brand-primary .name{font-weight:900;font-size:28px;color:var(--navy);text-transform:uppercase;letter-spacing:-.5px}
  .brand-url{position:absolute;left:42px;top:60px;font-weight:700;font-size:14px;color:var(--navy)}
  .brand-partner{right:18px;top:24px}
  .brand-partner .mark{width:18px;height:18px;border-radius:50%;background:var(--red)}
  .brand-partner .name{font-weight:900;font-size:24px;color:var(--red)}
  .partner-tag{position:absolute;right:18px;top:62px;font-weight:700;font-size:12px;color:var(--navy);letter-spacing:.5px}
</style>
</head>
<body>
<main class="infographic">
  <header class="masthead">
    <h2 class="old">OLD WORLD</h2>
    <div class="divider"></div>
    <h2 class="new">NEW WORLD</h2>
  </header>

  <section class="comparison">
    <div class="row">
      <div class="side side-old"></div><div class="side side-new"></div>
      <p class="label old">Handshakes</p>
      <div class="icon left icon-fill" style="width:52px;height:34px" role="img" aria-label="Handshake icon"></div>
      <div class="icon right icon-fill" style="width:40px;height:40px" role="img" aria-label="Waving hand icon"></div>
      <p class="label new">Waves</p>
    </div>

    <div class="row">
      <div class="side side-old"></div><div class="side side-new"></div>
      <p class="label old">High<br>Touch</p>
      <div class="icon left icon-fill" style="width:44px;height:46px" role="img" aria-label="High five hands icon"></div>
      <div class="icon right icon-fill" style="width:46px;height:46px;border-radius:50%" role="img" aria-label="No touching hand icon"></div>
      <p class="label new">Free<br>Touch</p>
    </div>

    <div class="row">
      <div class="side side-old"></div><div class="side side-new"></div>
      <p class="label old">Show<br>Your Face</p>
      <div class="icon left icon-fill" style="width:62px;height:34px" role="img" aria-label="Two people icon without masks"></div>
      <div class="icon right icon-fill" style="width:62px;height:34px" role="img" aria-label="Two people icon wearing facemasks"></div>
      <p class="label new">Hide Your Face<br>(Facemask)</p>
    </div>

    <div class="row">
      <div class="side side-old"></div><div class="side side-new"></div>
      <p class="label old">Work at<br>Work</p>
      <svg class="icon center" width="60" height="48" viewBox="0 0 60 48" aria-hidden="true">
        <rect x="21" y="2" width="18" height="8" rx="2" fill="none" stroke="var(--icon)" stroke-width="4"/>
        <rect x="2" y="10" width="56" height="36" rx="4" fill="var(--icon)"/>
        <rect x="2" y="24" width="56" height="3" fill="var(--icon-shade)"/>
        <rect x="26" y="21" width="8" height="9" rx="1" fill="var(--icon-shade)"/>
      </svg>
      <p class="label new">Work at<br>Home</p>
    </div>

    <div class="row">
      <div class="side side-old"></div><div class="side side-new"></div>
      <p class="label old">Open<br>Floor Plans</p>
      <svg class="icon center" width="46" height="46" viewBox="0 0 46 46" aria-hidden="true">
        <rect x="0" y="0" width="21" height="21" fill="var(--icon)"/>
        <rect x="25" y="0" width="21" height="21" fill="var(--icon)"/>
        <rect x="0" y="25" width="21" height="21" fill="var(--icon)"/>
        <rect x="25" y="25" width="21" height="21" fill="var(--icon)"/>
      </svg>
      <p class="label new">Separated<br>Floor Plans</p>
    </div>

    <div class="row supplies">
      <div class="side side-old"></div><div class="side side-new"></div>
      <p class="label old">Weeks of<br>Sanitation<br>Supplies on Hand</p>
      <span class="count old">2</span>
      <div class="icon center icon-fill" style="width:32px;height:66px" role="img" aria-label="Hand sanitizer pump bottle icon"></div>
      <span class="count new">3</span>
      <p class="label new">Months of<br>Sanitation<br>Supplies on Hand</p>
    </div>

    <div class="row">
      <div class="side side-old"></div><div class="side side-new"></div>
      <p class="label old">Common Areas<br>Built for Function</p>
      <div class="icon center icon-fill" style="width:70px;height:70px" role="img" aria-label="Safety barricade icon"></div>
      <p class="label new">Common Areas<br>Built for Safety</p>
    </div>

    <div class="row traffic">
      <div class="side side-old"></div><div class="side side-new"></div>
      <p class="label old">Unmanaged<br>People Traffic</p>
      <div class="icon center icon-fill" style="width:42px;height:66px" role="img" aria-label="Caution floor sign icon"></div>
      <p class="label new">Defined Pedestrian Paths – 1 Way Aisles at Retail</p>
    </div>
  </section>

  <footer class="sponsors">
    <div class="brand brand-primary"><span class="mark"></span><span class="name">Brentwick</span></div>
    <p class="brand-url">www.brentwickmercantile.com</p>
    <div class="brand brand-partner"><span class="mark"></span><span class="name">Ridgeline Supply</span></div>
    <p class="partner-tag">READY WHEN YOU ARE.</p>
  </footer>
</main>
</body>
</html>
```